Brochure Design Project

We are a payroll company. We offer a wide variety of products and services:
1. Payroll Processing
2. Employee Direct Deposit
3. Time and attendance
4. HR services
5. Employee Employee Benefits

I'd like to develop a one page template that uses a combination of our logo (attached), colors (attached) and possible a picture. The picture could be shown as an option as it may change based on the product or service.

Target Market(s)

Adults in the United States ages 22-50. Typically these people are accountants, human resource professionals or entrepreneurs. The payroll industry is dominated by 3 large payroll processors, KLV, Wendorn and Tolvaris. These companies are very impersonal and make it difficult to resolve issues when they arise. We have grown to over 400 clients by being the opposite of the big guys,

Industry/Entity Type

It Company

Font styles to use
Sans Serif

Requirements
Must have
• The brochure can be one or two pages.
Nice to have
• I'll know it when I see it but I can't describe it. I have attached a few brochures that have caught my eye.
Should not have
• No cartoons. No money signs. Hip, new, fresh are words I'd use to describe the winning product. Of the three people I described in my target market, the entrepreneur is the market I'd most like to target.

```html
<!DOCTYPE html>
<html lang="en">
<head>
<meta charset="utf-8">
<title>Quillfern Services – A New Approach to Payroll</title>
<link rel="stylesheet" href="https://fonts.googleapis.com/css2?family=Source+Sans+3:wght@400;600;700&display=swap">
<style>
  :root {
    --backdrop: #e9e6e1;
    --paper: #ffffff;
    --navy: #1f2a7d;
    --green: #8dc63f;
    --green-deep: #7db535;
    --ink: #3a3a3a;
    --muted: #6b6b6b;
    --photo-light: #d9e0ea;
    --photo-dark: #7d8ca3;
  }
  * { box-sizing: border-box; margin: 0; padding: 0; }
  html, body { width: 1200px; height: 1023px; overflow: hidden; }
  body {
    background: var(--backdrop);
    font-family: "Source Sans 3", Arial, sans-serif;
    color: var(--ink);
    position: relative;
  }
  .flyer {
    position: absolute; left: 232px; top: 55px;
    width: 685px; height: 887px;
    background: var(--paper);
  }
  .hero { position: absolute; left: 0; top: 0; width: 685px; height: 232px; }
  .hero svg { display: block; }
  .hero-copy {
    position: absolute; left: 411px; top: 74px; width: 236px; color: #fff;
  }
  .hero-title { font-size: 16.5px; font-weight: 700; letter-spacing: .2px; margin-bottom: 5px; }
  .hero-text { font-size: 9.9px; font-weight: 600; line-height: 12.2px; text-align: justify; }

  .column { position: absolute; top: 254px; width: 262px; }
  .column-left { left: 68px; }
  .column-right { left: 358px; }
  .section-title { color: var(--navy); font-size: 14px; font-weight: 600; margin-bottom: 5px; }
  .body-text { font-size: 12.3px; line-height: 14.8px; color: var(--ink); }
  .callout {
    margin: 14px 0 0 2px; width: 253px; height: 173px;
    background: var(--green); color: #fff;
    border-radius: 0 24px 0 24px;
    padding: 14px 16px 0 21px;
  }
  .callout-title { font-size: 13.5px; font-weight: 700; margin-bottom: 2px; }
  .callout-text { font-size: 11px; line-height: 13.5px; margin-bottom: 13px; }
  .gap-benefits { margin-top: 22px; }
  .gap-features { margin-top: 16px; }
  .gap-tech { margin-top: 16px; }
  .highlight { margin-top: 15px; color: var(--navy); font-weight: 700; font-size: 11.8px; line-height: 15px; }

  .brand {
    position: absolute; left: 0; width: 685px; top: 748px;
    display: flex; justify-content: center; align-items: center; gap: 8px;
  }
  .brand-mark { width: 14px; height: 14px; background: var(--navy); }
  .brand-name { color: var(--navy); font-size: 24px; font-weight: 700; }
  .footer { position: absolute; left: 0; width: 685px; text-align: center; }
  .footer-lead { top: 811px; font-size: 13px; color: var(--muted); }
  .footer-cta { top: 828px; font-size: 15px; font-weight: 700; color: #2a2a2a; }
</style>
</head>
<body>
  <article class="flyer">
    <header class="hero">
      <svg width="685" height="232" viewBox="0 0 685 232">
        <defs>
          <linearGradient id="photoTone" x1="0" y1="0" x2="1" y2="1">
            <stop offset="0" stop-color="#d9e0ea"/>
            <stop offset=".5" stop-color="#aab6c7"/>
            <stop offset="1" stop-color="#7d8ca3"/>
          </linearGradient>
          <linearGradient id="greenTone" x1="0" y1="0" x2="1" y2="1">
            <stop offset="0" stop-color="#7db535"/>
            <stop offset="1" stop-color="#8dc63f"/>
          </linearGradient>
        </defs>
        <polygon points="0,0 433,0 308,232 0,232" fill="url(#photoTone)" role="img" aria-label="Photo of stacked coins on a financial chart printout"/>
        <polygon points="446,0 685,0 685,232 321,232" fill="url(#greenTone)" role="img" aria-label="Green-tinted photo of calculator keys"/>
      </svg>
      <div class="hero-copy">
        <h1 class="hero-title">A New Approach to Payroll</h1>
        <p class="hero-text">Quillfern Services is a complete business payroll solution designed to help you easily pay your employees, file your taxes on time and comply with all state and federal payroll requirements. Additionally, it offers a suite of integrated services that can further streamline your business practices.</p>
      </div>
    </header>

    <section class="column column-left">
      <h2 class="section-title">Quillfern Services</h2>
      <p class="body-text">il et eius nonsequam atessec tatios auteem ut est aut aut lita quis volendem qfue nit acea nonsedi um as m quae nost volorquae fnost volorporrum que porem ququase nost volorporrum fque porem quporrum que porem quatur?</p>
      <aside class="callout">
        <h3 class="callout-title">Turiasp dolupta tiatur suntio.</h3>
        <p class="callout-text">Nem exerion are coribus in deriti quunt deriti quunt deriti quunt molorrovidem volor remqderiti quunt atio et voluptatem. Ut laborit fugia peribus dolo cus.</p>
        <p class="callout-text">voluptatem. Ut laborit fugia peribus dolo cuvoluptatem. Ut laborit fugia peribus dolo cu voluptatem. Ut laborit fugia peribus dolo cus. voluptatem.</p>
      </aside>
      <h2 class="section-title gap-benefits">Benefits of Quillfern Services</h2>
      <p class="body-text">voluptam, quae nossequis et undis volupta tibam ditm voluptat mos ut et auda doreemque vendips andenis sam quam fugiti aut quo emaximenia eit, sim ab ipsam fuga. Nequid mooritatsdsm qunddia it, sim ania expelit, sim adm, apid quieame dolum entempo rporum fugiatiis inihil mad volupta upta tempellescid. enisquia tibudsdam dita quo berum voluptat mos ut et auda doloremqddsaue vendips</p>
    </section>

    <section class="column column-right">
      <p class="body-text">andenis sam quam ftibusdam ditdsdsa quo berum voluptat mserdos ut et auda doloremque vendips andenis sam quam fugiti aut dsdsaquo maximenia expelit, sim ab ipsa expelit, sim afdfdb ipsam fuga.</p>
      <h2 class="section-title gap-features">Features</h2>
      <p class="body-text">sandisi mporuptatem a num et volum et mo tet aut laborerum aceribus, odicias itiscip suscium, coritem. Epelluptam a vit que viducilia voluptatem cupta cuptian tissunt estiae vent, serferum est et labo. ?</p>
      <h2 class="section-title gap-tech">Service-Driven Technology</h2>
      <p class="body-text">net reptaerum sincto occae et fugit, explis magnat es rem laudit pores reptist excepta quibus, sectate oditaatum ipidebis es accusda santures aut lant laci tecus consequas assitia nditiur? Quiatum ipidebis ea santures aut lant laci tecus consequas assitia nditiur? Quiatio con nos dolum fugiatiis ex et endis rectatiore volupta turibus ipis et laut faceatia veniend .</p>
      <p class="highlight">tibusdam dita quo berum voluptat mos ut<br>et auda doltta quo berum o berum vendips<br>andenis sam quam fugiti aut quo mata quo<br>berum ximenia expelit,ta quo berum sim ab<br>ipsam fuga.</p>
    </section>

    <div class="brand">
      <span class="brand-mark"></span>
      <span class="brand-name">Quillfern Partners</span>
    </div>
    <p class="footer footer-lead">For more information about Quillfern Services,</p>
    <p class="footer footer-cta">Please call 855-555-0142 or visit quillfern.example/payroll-services</p>
  </article>
</body>
</html>
```